Q spot menu

single page
we are located right across from Larkfield Grounds Gullwings ballpark
Menu has to be double sided 11”x17”

APPETIZERS
Guacamole and Chips $14 HH $9
House-made guacamole and tortilla chips. Served with pico de gallo, queso fresco and salsa.

Grand Slam Nachos $18 HH $13
House-made tortilla chips smothered with Jack and cheddar cheeses, your choice of meat (seasoned ground beef, chicken, pork carnitas, or veggies, beans, and jalapeños. Served with sour cream, guacamole, pico de gallo and salsa.

Quesadilla 15 HH$10
Flour tortilla filled with Jack and cheddar cheeses, your choice of meat (seasoned ground beef, chicken, pork carnitas, or veggies. folded in half and cooked golden brown. Served with sour cream and guacamole.

Beef Sliders $15
Premium Angus beef, Jack cheese, sauteed onions, rajas, tomato, spring mix, house mayo and chipotle aioli on a brioche bun.

Chicken Strips $15 HH $10
House-battered and breaded chicken breast strips. Served with your choice of dressing and fries. SUB ONION RINGS +$3

Corvo Wings $15 HH $10
7 Jumbo-size drums and flats tossed in your choice of sauce (BBQ, buffalo, mango habanero, or lemon pepper) or dry. Served with carrots, celery sticks, and your choice of dressing.

Onion Rings $9
Jumbo onion rings. Served with your choice of dressing.

Mozzarella Sticks $10
7 Breaded and fried mozzarella cheese sticks. Served with marinara sauce and ranch dressing.

SALADS
All salads are served with your choice of dressing (Ranch, Blue cheese, Honey mustard, or Balsamic vinaigrette).

Dinner Salad $9
Mixed greens, tomatoes, onions, cheese and carrots.

Taco Salad $17
Large flour tortilla crispy shell filled with your choice of meat (seasoned ground beef, pork carnitas, chicken or veggies, beans, lettuce, tomatoes, jalapeños and cheese. Topped with sour cream, pico de gallo and salsa.

Ahi Tuna Salad $19
Pan-seared Ahi tuna steak (6 oz.) on a bed of spring mix, tomatoes, beets, orange slices and sesame seeds.

Salmon Salad $20
Pan-seared salmon filet, on a bed of mixed greens, tomatoes, onions, avocado slices, carrots and cheese.
BURGERS ( 8oz)
Served with fries. (add an egg +$2)
El Gran Tio Burger $17
Verified Prairie Stock patty, cheddar cheese, and caramelized onions, mayo, lettuce, tomato, avocado and a fried jalapeño.

All-American Burger $16
Verified Prairie Stock patty, Cheddar cheese, mayo, lettuce, tomato, onion and pickles.
- Add bacon +$3
- Add an egg +$2

Whiskey Burger $17
Verified Prairie Stock patty, bacon, caramelized onions and Swiss cheese, mayo and house-made Moss Haverty whiskey sauce.

Mushroom Swiss Burger $17
Verified Prairie Stock patty, mayo, Swiss cheese, bacon, and mushrooms on ciabatta bread.

Veggie Burger $16 (VG)
Black bean patty on a pretzel bun with mayo, lettuce, tomato, onion, pickles, and avocado.

Salmon Burger $17
Pan-seared salmon filet (6 oz.) on a pretzel bun with mayo, lettuce, tomato, avocado and chipotle aioli.

Grilled Chicken Sandwich $16
Mayo, grilled chicken breast on ciabatta bread with lettuce, tomato, onions, pickles, and avocado.

SOUTH OF THE BORDER
3 Street Tacos 12 HH $7
seasoned ground beef, pork carnitas, chicken or veggies, pico de gallo and salsa. ADD GUAC +$3

2-lb. Burrito $15
Flour tortilla wrapped around your choice of meat seasoned ground beef, pork, chicken, or veggies. rice, beans, guacamole, sour cream, salsa and Jack and cheddar cheeses.

Chile Colorado Burrito $16
Special Trim Beef simmered in a house-made Chile Colorado sauce, rice and beans wrapped in a flour tortilla. Topped with sour cream.

EVENT MENU
Grand Slam Nachos $18
House-made tortilla chips smothered with Jack and cheddar cheeses, your choice of meat (seasoned ground beef, pork, chicken or veggies. beans and jalapeños. Served with sour cream, guacamole, pico de gallo and salsa.

3 Street Tacos $12
Your choice of meat seasoned ground beef, pork carnitas, chicken, or veggies, pico de gallo and salsa.

2-lb. Burrito $15
Flour tortilla wrapped around your choice of meat (seasoned ground beef, pork carnitas or grilled chicken) or veggies, rice, beans, guacamole, sour cream, salsa and Jack and cheddar cheeses.

Quesadilla $15
Flour tortilla filled with Jack and cheddar cheeses, your choice of meat (seasoned ground beef, pork carnitas, chicken or veggies, folded in half and cooked golden brown. Served with guacamole, pico de gallo and sour cream.

Taco Salad $17

Corvo Wings $15
7 Jumbo-size drums and flats tossed in your choice of sauce (BBQ, buffalo, mango habanero, or lemon pepper) or dry. Served with carrot and celery sticks.

Chicken Strips $15
House-battered and breaded chicken breast strips. Served with fries and your choice dressing.

All-American Burger $16
Verified Prairie Stock patty, Cheddar cheese, with mayo, lettuce, tomato, onion and pickles.
- Add bacon +$3
- Add avocado +$3

Whiskey Burger $17
Verified Prairie Stock patty, bacon, caramelized onions and Swiss cheese, with mayo and house-made Moss Haverty whiskey sauce.

Veggie Burger $16
Black bean patty, with mayo, lettuce, tomato, onion, pickles and avocado.

SIDES
basket of French fries $7
Rice $5
Beans $5
Sour cream $1
Avocado $4
Guacamole $7
Salsa 4oz. $2
Dressing $1

HOUSE SPECIALTIES
Carne Asada Entrée $23
Charbroiled skirt steak, cooked to order. Served with rice, beans, pico de gallo, salsa, sour cream, guacamole and tortillas.

Chile Colorado Entrée $18
Special Trim Beef simmered in a house-made Chile Colorado sauce. Served with rice, beans, sour cream and tortillas.

Pork Shank (Wednesdays only, until sold out) $24
Slow-baked pork shank (fork tender and fall-off-the-bone moist). Served with rice, beans, pico de gallo, salsa and tortillas. Ask your server about availability.

BEVERAGES
Soft Drinks $3.50
Zolta, Diet Zolta, Brook Fizz,
Juice $5
Orange, cranberry, pineapple, grapefruit
Milk $4

HAPPY HOUR
Mon- Fri 2-5pm & 10-Close
Any draft beer $2 off
Selected appetizers $5 off
Well drinks $2 off
Wine $2 off

Daily specials 11:30 am - 5 pm

Margarita Monday $2 off /Burgers 20%off
Tacos Tuesday $5 off /Tequila Casa Verano 1871 $19.42
Wing Wednesday $5 Off / whiskey $2 Off
Thirsty Thursday Any draft beer $5/Nachos $5 off
Emberloch Friday $6 shot /Chile colorado burrito 20%off
Saturday and Sunday Brunch 10am-1pm. Mimosas and Bloody Marrys

Please make sure that you put this note on both pages * *CONSUMING RAW OR UNDERCOOKED MEATS, POULTRY, SEAFOOD, SHELLFISH, OR EGGS MAY INCREASE YOUR RISK OF FOODBORNE ILLNESS, ESPECIALLY IF YOU HAVE CERTAIN MEDICAL CONDITIONS.

Items that have eggs or meet HAS TO BE MARKED WITH AN ASTERISK*

AUTOMATIC 20% GRATUITY ON GROUPS OF 5 OR MORE. ALL ORDERS TO GO +$1

Target Market(s)

Young crowd

Industry/Entity Type

Sports bar

Colors
FFC000
F8CF3A
FAE287
FDF2CF
FEFAEE

Requirements
Must have
• Entire menu
Nice to have
• Menu has to be simple bat VERY attractive

```html
<!DOCTYPE html>
<html lang="en">
<head>
<meta charset="utf-8">
<title>Q Spot Sports Bar &amp; Grill – Menu</title>
<link rel="stylesheet" href="https://fonts.googleapis.com/css2?family=Alfa+Slab+One&family=Montserrat:wght@400;500;600;700;800&display=swap">
<style>
:root{
  --backdrop:#e4e4e4;
  --page:#141414;
  --page-2:#1f1f1f;
  --gold-dark:#8c7440;
  --gold:#c9a862;
  --gold-light:#e3cd92;
  --amber:#ffc000;
  --hh:#f0a32a;
  --white:#ffffff;
  --muted:#d8d8d8;
  --red:#d41f26;
}
*{margin:0;padding:0;box-sizing:border-box}
html,body{width:685px;height:1200px;overflow:hidden;background:var(--backdrop)}
body{position:relative;font-family:"Montserrat",sans-serif;color:var(--white)}

.page{position:absolute;left:155px;width:610px;height:940px;transform:scale(.6148);transform-origin:0 0;
  background:var(--page);overflow:hidden;box-shadow:0 6px 18px rgba(0,0,0,.35)}
.page--front{top:14px}
.page--back{top:608px}

.bar-photo{position:absolute;inset:0 0 auto 0;height:430px;
  background:linear-gradient(180deg,#3a3128 0%,#2a241f 35%,#181614 75%,var(--page) 100%)}
.texture{position:absolute;inset:430px 0 0 0;background:linear-gradient(180deg,var(--page),var(--page-2) 60%,#101010)}

.food-photo{position:absolute;left:0;right:0;bottom:0;height:125px;
  background:linear-gradient(90deg,#d9a43a 0%,#b56a2b 18%,#e8e0cc 32%,#4d8b2c 45%,#d9a957 58%,#f1ece0 72%,#b8552e 86%,#4f8a2a 100%)}
.page--back .food-photo{height:95px;
  background:linear-gradient(90deg,#4f8a2a 0%,#b8332a 14%,#e9e3d6 32%,#e39a3a 46%,#c8a07a 58%,#f1ece0 72%,#d9722e 88%,#4f8a2a 100%)}
.cocktail-photo{position:absolute;left:375px;top:232px;width:205px;height:140px;border-radius:6px;
  background:radial-gradient(circle at 25% 40%,#e0466a 0 18%,transparent 30%),radial-gradient(circle at 60% 45%,#ee6a3a 0 16%,transparent 28%),radial-gradient(circle at 82% 40%,#f2c12e 0 20%,transparent 32%),linear-gradient(180deg,#262220,#151515)}

.brand{position:absolute;left:36px;top:52px;display:flex;align-items:center;gap:6px}
.brand__mark{width:14px;height:14px;border-radius:50%;background:var(--white)}
.brand__name{font-family:"Montserrat",sans-serif;font-weight:800;font-size:30px;letter-spacing:1px;color:var(--white)}

.title{position:absolute;left:345px;top:44px;width:232px;text-align:center}
.title__word{font-family:"Alfa Slab One",serif;font-size:60px;line-height:68px;letter-spacing:0;white-space:nowrap;color:var(--white)}
.title__sub{display:block;margin-top:2px;padding:3px 0;border-top:2px solid var(--white);border-bottom:2px solid var(--white);
  font-family:"Alfa Slab One",serif;font-size:17px;letter-spacing:.5px;white-space:nowrap;color:var(--white)}

.section-tag{position:absolute;height:30px;display:flex;align-items:center;justify-content:center;
  font-family:"Alfa Slab One",serif;font-size:15px;letter-spacing:.5px;color:var(--white);
  background:linear-gradient(90deg,transparent 0,var(--gold-dark) 6%,var(--gold) 35%,var(--gold-light) 60%,var(--gold) 85%,transparent 100%);
  border-radius:3px}

.list{position:absolute;display:flex;flex-direction:column}
.item{display:grid;grid-template-columns:1fr 40px 46px;align-items:center;column-gap:6px}
.item__name{font-weight:700;font-size:6.2px;text-transform:uppercase;letter-spacing:.2px}
.item__desc{font-size:5.9px;line-height:7.2px;color:var(--muted)}
.price{font-weight:600;font-size:6.5px;text-align:center;color:var(--white)}
.hh{font-weight:600;font-size:6.5px;text-align:center;color:var(--hh)}
.accent{color:var(--hh)}

.rule{position:absolute;border-left:1px dashed rgba(201,168,98,.7)}

.appetizers{left:34px;top:186px;width:540px;gap:11.5px}
.salads{left:34px;top:490px;width:252px;gap:13px}
.salads .item{grid-template-columns:1fr 36px}
.border-list{left:315px;top:490px;width:262px;gap:14px}
.sides{left:317px;top:690px;width:100px;gap:1.5px}
.sides .row,.bev .row{display:flex;justify-content:space-between;font-size:6px;font-weight:600;text-transform:uppercase}
.bev{left:453px;top:690px;width:120px;gap:5px}

.notice{position:absolute;left:36px;width:215px}
.notice__legal{font-size:5.6px;line-height:7px;text-transform:uppercase;color:var(--muted)}
.notice__egg{margin-top:6px;font-size:5.6px;line-height:7px;color:var(--hh)}
.notice__grat{margin-top:4px;font-weight:700;font-size:8px;line-height:10px;text-transform:uppercase;width:155px}
.to-go{position:absolute;width:44px;height:44px;border-radius:50%;background:var(--red);color:var(--white);
  display:flex;flex-direction:column;align-items:center;justify-content:center;text-align:center;box-shadow:0 0 0 2px rgba(255,255,255,.25)}
.to-go small{font-size:4px;font-weight:700;line-height:4.5px;text-transform:uppercase}
.to-go b{font-size:12px;font-weight:800;line-height:13px}

.burgers{left:34px;top:95px;width:300px;gap:10px}
.burgers .item,.specialties .item{grid-template-columns:1fr 36px}
.lead{position:absolute;left:34px;top:78px;font-size:9px;font-weight:600}
.specialties{left:350px;top:88px;width:240px;gap:10px}
.event{left:34px;top:383px;width:556px;gap:8.5px}
.event .item{grid-template-columns:1fr 46px}

.hh-tag{position:absolute;left:188px;top:666px;background:var(--white);color:#222;font-size:6px;font-weight:700;padding:3px 10px 3px 8px;clip-path:polygon(0 0,100% 10%,96% 100%,2% 88%)}
.hh-tag em{font-style:normal;color:var(--red)}
.hh-grid{position:absolute;left:34px;top:712px;display:grid;grid-template-columns:120px 50px 60px 60px 40px;row-gap:4px;font-size:6.3px;font-weight:600;text-transform:uppercase}
.hh-grid .off{color:var(--hh)}
.daily-tag{position:absolute;left:36px;top:748px;background:var(--white);color:#222;font-size:5.8px;font-weight:700;padding:3px 12px;border-radius:10px}
.daily-tag em{font-style:normal;color:var(--red)}
.daily{position:absolute;left:36px;top:766px;width:340px;display:grid;grid-template-columns:1fr 50px;row-gap:2px;font-size:6.4px;font-weight:700;text-transform:uppercase}
.daily .deal{color:var(--red);text-align:right}
.daily .brunch{grid-column:1 / -1;color:var(--amber);text-transform:none;font-weight:600}
</style>
</head>
<body>

<section class="page page--front">
  <div class="bar-photo" role="img" aria-label="Dimly lit bar with beer taps in the background"></div>
  <div class="texture"></div>

  <div class="brand"><span class="brand__mark"></span><span class="brand__name">Q SPOT</span></div>

  <header class="title">
    <div class="title__word">MENU</div>
    <span class="title__sub">SPORTS BAR &amp; GRILL</span>
  </header>

  <div class="section-tag" style="left:30px;top:146px;width:160px">APPETIZERS</div>
  <div class="rule" style="left:480px;top:186px;height:235px"></div>
  <div class="rule" style="left:526px;top:186px;height:235px"></div>

  <div class="list appetizers">
    <div class="item"><div><div class="item__name">Guacamole and Chips</div><div class="item__desc">House-made guacamole and tortilla chips. Served with pico de gallo, queso fresco and salsa.</div></div><span class="price">$14</span><span class="hh">HH $9</span></div>
    <div class="item"><div><div class="item__name">Grand Slam Nachos</div><div class="item__desc">House-made tortilla chips smothered with Jack and cheddar cheeses, your choice of meat (seasoned ground beef, chicken, pork carnitas, or veggies, beans, and jalapeños. Served with sour cream, guacamole, pico de gallo and salsa.</div></div><span class="price">$18</span><span class="hh">HH $13</span></div>
    <div class="item"><div><div class="item__name">Quesadilla</div><div class="item__desc">Flour tortilla filled with Jack and cheddar cheeses, your choice of meat (seasoned ground beef, chicken, pork carnitas, or veggies. folded in half and cooked golden brown. Served with sour cream and guacamole.</div></div><span class="price">$15</span><span class="hh">HH $10</span></div>
    <div class="item"><div><div class="item__name">Beef Sliders</div><div class="item__desc">Premium Angus beef, Jack cheese, sauteed onions, rajas, tomato, spring mix, house mayo and chipotle aioli on a brioche bun.</div></div><span></span><span class="hh">$15</span></div>
    <div class="item"><div><div class="item__name">Chicken Strips</div><div class="item__desc">House-battered and breaded chicken breast strips. Served with your choice of dressing and fries. SUB ONION RINGS +$3</div></div><span class="price">$15</span><span class="hh">HH $10</span></div>
    <div class="item"><div><div class="item__name">Corvo Wings $15 HH</div><div class="item__desc">7 Jumbo-size drums and flats tossed in your choice of sauce (BBQ, buffalo, mango habanero, or lemon pepper) or dry. Served with carrots, celery sticks, and your choice of dressing.</div></div><span class="price">$15</span><span class="hh">HH $10</span></div>
    <div class="item"><div><div class="item__name">Onion Rings</div><div class="item__desc">Jumbo onion rings. Served with your choice of dressing.</div></div><span></span><span class="hh">$9</span></div>
    <div class="item"><div><div class="item__name">Mozzarella Sticks $10</div><div class="item__desc">7 Breaded and fried mozzarella cheese sticks. Served with marinara sauce and ranch dressing.</div></div><span></span><span class="hh">$10</span></div>
  </div>

  <div class="section-tag" style="left:30px;top:450px;width:160px">SALADS</div>
  <div class="list salads">
    <div class="item"><div><div class="item__name" style="text-transform:none">All salads are served with your choice of dressing</div><div class="item__desc">(Ranch, Blue cheese, Honey mustard, or Balsamic vinaigrette).</div></div><span class="hh">$9</span></div>
    <div class="item"><div><div class="item__name">Dinner Salad</div><div class="item__desc">Mixed greens, tomatoes, onions, cheese and carrots.</div></div><span class="hh">$9</span></div>
    <div class="item"><div><div class="item__name">Taco Salad</div><div class="item__desc">Large flour tortilla crispy shell filled with your choice of meat (seasoned ground beef, pork carnitas, chicken or veggies, beans, lettuce, tomatoes, jalapeños and cheese. Topped with sour cream, pico de gallo and salsa.</div></div><span class="hh">$17</span></div>
    <div class="item"><div><div class="item__name">Ahi Tuna Salad</div><div class="item__desc">Pan-seared Ahi tuna steak (6 oz.) on a bed of spring mix, tomatoes, beets, orange slices and sesame seeds.</div></div><span class="hh">$19</span></div>
    <div class="item"><div><div class="item__name">Salmon Salad</div><div class="item__desc">Pan-seared salmon filet, on a bed of mixed greens, tomatoes, onions, avocado slices, carrots and cheese.</div></div><span class="hh">$20</span></div>
  </div>

  <div class="section-tag" style="left:310px;top:450px;width:240px">SOUTH OF THE BORDER</div>
  <div class="rule" style="left:483px;top:490px;height:140px"></div>
  <div class="list border-list">
    <div class="item"><div><div class="item__name" style="text-transform:none">3 Street Tacos</div><div class="item__desc">seasoned ground beef, pork carnitas, chicken or veggies, pico de gallo and salsa. ADD GUAC +$3</div></div><span class="price">$12</span><span class="hh">HH$7</span></div>
    <div class="item"><div><div class="item__name">2-lb. Burrito $15</div><div class="item__desc">Flour tortilla wrapped around your choice of meat seasoned ground beef, pork, chicken, or veggies. rice, beans, guacamole, sour cream, salsa and Jack and cheddar cheeses.</div></div><span></span><span class="hh">$15</span></div>
    <div class="item"><div><div class="item__name">Chile Colorado Burrito</div><div class="item__desc">Special Trim Beef simmered in a house-made Chile Colorado sauce, rice and beans wrapped in a flour tortilla. Topped with sour cream.</div></div><span></span><span class="hh">$16</span></div>
  </div>

  <div class="section-tag" style="left:313px;top:655px;width:100px">SIDES</div>
  <div class="list sides">
    <div class="row"><span>Basket of French fries $7</span><span class="accent">$7</span></div>
    <div class="row"><span>Rice $5</span><span class="accent">$5</span></div>
    <div class="row"><span>Beans $5</span><span class="accent">$5</span></div>
    <div class="row"><span>Sour cream $1</span><span class="accent">$1</span></div>
    <div class="row"><span>Avocado $4</span><span class="accent">$4</span></div>
    <div class="row"><span>Guacamole $7</span><span class="accent">$7</span></div>
    <div class="row"><span>Salsa 4oz. $2</span><span class="accent">$2</span></div>
    <div class="row"><span>Dressing $1</span><span class="accent">$1</span></div>
  </div>

  <div class="section-tag" style="left:448px;top:655px;width:125px">BEVERAGES</div>
  <div class="list bev">
    <div><div class="row"><span>Soft Drinks</span><span class="accent">$3.50</span></div><div class="item__desc">Zolta, Diet Zolta, Brook Fizz,</div></div>
    <div><div class="row"><span>Juice</span><span class="accent">$5</span></div><div class="item__desc">Orange, cranberry, pineapple, grapefruit</div></div>
    <div class="row"><span>Milk</span><span class="accent">$4</span></div>
  </div>

  <div class="notice" style="top:712px">
    <p class="notice__legal">* *Consuming raw or undercooked meats, poultry, seafood, shellfish, or eggs may increase your risk of foodborne illness, especially if you have certain medical conditions.</p>
    <p class="notice__egg">Items that have eggs or meet HAS TO BE MARKED WITH AN ASTERISK*</p>
    <p class="notice__grat">Automatic 20% gratuity on groups of 5 or more.</p>
  </div>
  <div class="to-go" style="left:196px;top:752px"><small>All order<br>to go</small><b>+$1</b></div>

  <div class="food-photo" role="img" aria-label="Plates of chicken strips with fries, nachos and a taco salad with fresh lettuce"></div>
</section>

<section class="page page--back">
  <div class="bar-photo" role="img" aria-label="Back bar shelves with bottles and glassware"></div>
  <div class="texture"></div>

  <div class="section-tag" style="left:30px;top:42px;width:160px">BURGERS (8OZ)</div>
  <p class="lead">Served with fries. <span style="color:var(--amber)">(add an egg +$2)</span></p>
  <div class="list burgers">
    <div class="item"><div><div class="item__name">El Gran Tio Burger</div><div class="item__desc">Verified Prairie Stock patty, cheddar cheese, and caramelized onions, mayo, lettuce, tomato, avocado and a fried jalapeño.</div></div><span class="hh">$17</span></div>
    <div class="item"><div><div class="item__name">All-American Burger</div><div class="item__desc">Verified Prairie Stock patty, Cheddar cheese, mayo, lettuce, tomato, onion and pickles.<br>- Add bacon +$3<br>- Add an egg +$2</div></div><span class="hh">$16</span></div>
    <div class="item"><div><div class="item__name">Whiskey Burger</div><div class="item__desc">Verified Prairie Stock patty, bacon, caramelized onions and Swiss cheese, mayo and house-made Moss Haverty whiskey sauce.</div></div><span class="hh">$17</span></div>
    <div class="item"><div><div class="item__name">Mushroom Swiss Burger</div><div class="item__desc">Verified Prairie Stock patty, mayo, Swiss cheese, bacon, and mushrooms on ciabatta bread.</div></div><span class="hh">$17</span></div>
    <div class="item"><div><div class="item__name">Veggie Burger (VG)</div><div class="item__desc">Black bean patty on a pretzel bun with mayo, lettuce, tomato, onion, pickles, and avocado.</div></div><span class="hh">$16</span></div>
    <div class="item"><div><div class="item__name">Salmon Burger</div><div class="item__desc">Pan-seared salmon filet (6 oz.) on a pretzel bun with mayo, lettuce, tomato, avocado and chipotle aioli.</div></div><span class="hh">$17</span></div>
    <div class="item"><div><div class="item__name">Grilled Chicken Sandwich</div><div class="item__desc">Mayo, grilled chicken breast on ciabatta bread with lettuce, tomato, onions, pickles, and avocado.</div></div><span class="hh">$16</span></div>
  </div>

  <div class="section-tag" style="left:345px;top:42px;width:200px">HOUSE SPECIALTIES</div>
  <div class="list specialties">
    <div class="item"><div><div class="item__name">Carne Asada Entrée</div><div class="item__desc">Charbroiled skirt steak, cooked to order. Served with rice, beans, pico de gallo, salsa, sour cream, guacamole and tortillas.</div></div><span class="hh">$23</span></div>
    <div class="item"><div><div class="item__name">Chile Colorado Entrée</div><div class="item__desc">Special Trim Beef simmered in a house-made Chile Colorado sauce. Served with rice, beans, sour cream and tortillas.</div></div><span class="hh">$18</span></div>
    <div class="item"><div><div class="item__name">Pork Shank (Wednesdays only, until sold out)</div><div class="item__desc">Slow-baked pork shank (fork tender and fall-off-the-bone moist). Served with rice, beans, pico de gallo, salsa and tortillas. Ask your server about availability.</div></div><span class="hh">$24</span></div>
  </div>

  <div class="cocktail-photo" role="img" aria-label="Three colourful margarita cocktails"></div>

  <div class="section-tag" style="left:30px;top:342px;width:160px">EVENT MENU</div>
  <div class="list event">
    <div class="item"><div><div class="item__name">Grand Slam Nachos</div><div class="item__desc">House-made tortilla chips smothered with Jack and cheddar cheeses, your choice of meat (seasoned ground beef, pork, chicken or veggies. beans and jalapeños. Served with sour cream, guacamole, pico de gallo and salsa.</div></div><span class="hh">$18</span></div>
    <div class="item"><div><div class="item__name">3 Street Tacos</div><div class="item__desc">Your choice of meat seasoned ground beef, pork carnitas, chicken, or veggies, pico de gallo and salsa.</div></div><span class="hh">$12</span></div>
    <div class="item"><div><div class="item__name">2-lb. Burrito</div><div class="item__desc">Flour tortilla wrapped around your choice of meat (seasoned ground beef, pork carnitas or grilled chicken) or veggies, rice, beans, guacamole, sour cream, salsa and Jack and cheddar cheeses.</div></div><span class="hh">$15</span></div>
    <div class="item"><div><div class="item__name">Quesadilla</div><div class="item__desc">Flour tortilla filled with Jack and cheddar cheeses, your choice of meat (seasoned ground beef, pork carnitas, chicken or veggies, folded in half and cooked golden brown. Served with guacamole, pico de gallo and sour cream.</div></div><span class="hh">$15</span></div>
    <div class="item"><div><div class="item__name">Taco Salad</div><div class="item__desc">Large flour tortilla crispy shell filled with your choice of meat (seasoned ground beef, pork carnitas, chicken or veggies, beans, lettuce, tomatoes, jalapeños and cheese. Topped with sour cream, pico de gallo and salsa.</div></div><span class="hh">$17</span></div>
    <div class="item"><div><div class="item__name">Corvo Wings</div><div class="item__desc">7 Jumbo-size drums and flats tossed in your choice of sauce (BBQ, buffalo, mango habanero, or lemon pepper) or dry. Served with carrot and celery sticks.</div></div><span class="hh">$15</span></div>
    <div class="item"><div><div class="item__name">Chicken Strips</div><div class="item__desc">House-battered and breaded chicken breast strips. Served with fries and your choice dressing.</div></div><span class="hh">$15</span></div>
    <div class="item"><div><div class="item__name">All-American Burger</div><div class="item__desc">Verified Prairie Stock patty, Cheddar cheese, with mayo, lettuce, tomato, onion and pickles.<br>- Add bacon +$3<br>- Add avocado +$3</div></div><span class="hh">$16</span></div>
    <div class="item"><div><div class="item__name">Whiskey Burger</div><div class="item__desc">Verified Prairie Stock patty, bacon, caramelized onions and Swiss cheese, with mayo and house-made Moss Haverty whiskey sauce.</div></div><span class="hh">$17</span></div>
    <div class="item"><div><div class="item__name">Veggie Burger</div><div class="item__desc">Black bean patty, with mayo, lettuce, tomato, onion, pickles and avocado.</div></div><span class="hh">$16</span></div>
  </div>

  <div class="section-tag" style="left:30px;top:660px;width:150px">HAPPY HOUR</div>
  <div class="hh-tag">Mon- Fri <em>2-5pm</em> &amp; <em>10-Close</em></div>
  <div class="hh-grid">
    <span>Any draft beer</span><span class="off">$2 OFF</span><span></span><span>Well drinks</span><span class="off">$2 OFF</span>
    <span>Selected appetizers</span><span class="off">$5 OFF</span><span></span><span>Wine</span><span class="off">$2 OFF</span>
  </div>
  <div class="daily-tag">Daily specials <em>11:30 am - 5 pm</em></div>
  <div class="daily">
    <span>Margarita Monday $2 off /Burgers</span><span class="deal">20%OFF</span>
    <span>Tacos Tuesday $5 off /Tequila Casa Verano 1871</span><span class="deal">$19.42</span>
    <span>Wing Wednesday $5 off / Whiskey</span><span class="deal">$2 OFF</span>
    <span>Thirsty Thursday any draft beer $5/Nachos</span><span class="deal">$5 OFF</span>
    <span>Emberloch Friday $6 shot /Chile Colorado burrito</span><span class="deal">20%OFF</span>
    <span class="brunch">Saturday and Sunday Brunch 10am-1pm. Mimosas and Bloody Marrys</span>
  </div>

  <div class="notice" style="left:402px;top:668px;width:185px">
    <p class="notice__legal">* *Consuming raw or undercooked meats, poultry, seafood, shellfish, or eggs may increase your risk of foodborne illness, especially if you have certain medical conditions.</p>
    <p class="notice__egg">Items that have eggs or meet HAS TO BE MARKED WITH AN ASTERISK*</p>
    <p class="notice__grat" style="font-size:10px;line-height:12px;width:135px">Automatic 20% gratuity on groups of 5 or more</p>
  </div>
  <div class="to-go" style="left:545px;top:738px"><small>All order<br>to go</small><b>+$1</b></div>

  <div class="food-photo" role="img" aria-label="Plates of enchiladas, grilled salmon with orange slices and a smothered burrito"></div>
</section>

</body>
</html>
```